Pecan Ridge Paving. Chip Seal Done Right

I need my card to have all my basic information on it. Keep it simple. Include web site, phone number and email address. Include phrase Chip Seal Done Right or Pecan Ridge’s Top Paving Company. Keep card simple. Include color and logo. Put all contact info on card. Make card simple and not complicated.

Here is infuriation yo out in business card

Dale R. Whitmore
830.555.0173 cell phone
Dalewhitmore7@mailbarn.net
www.pecanridgepaving.net

Target Market(s)

Hill Country Texas USA

Industry/Entity Type

Road chip seal

Contact Information for Business Card

We chip seal roads for ranches and property owners

Font styles to use
Serif
Sans Serif
Decorative
Script

Colors
0054AA
0677BA
7BADD7
CADEEF
E8F1F8
EB3D1F
EC4F4E
F09395
F8D3D4
FCEDEE

Requirements
Must have
• Keep it simply
Nice to have
• Logo and all basic info

```html
<!DOCTYPE html>
<html lang="en">
<head>
<meta charset="utf-8">
<title>Pecan Ridge Paving – Business Card</title>
<link rel="stylesheet" href="https://fonts.googleapis.com/css2?family=Lato:wght@400;700;900&family=Oswald:wght@500&display=swap">
<style>
  :root {
    --backdrop: #1b1b1d;
    --card-navy: #172050;
    --accent-red: #b21f2d;
    --text-white: #ffffff;
    --divider: #8a90b0;
  }
  * { box-sizing: border-box; margin: 0; padding: 0; }
  html, body {
    width: 1200px; height: 900px; overflow: hidden;
    background: var(--backdrop);
  }
  .canvas {
    position: relative; width: 1200px; height: 900px;
    display: flex; flex-direction: column; align-items: center; justify-content: center;
    gap: 40px;
  }
  .card {
    position: relative; width: 600px; height: 343px;
    background: var(--card-navy);
    box-shadow: 0 10px 28px rgba(0,0,0,.55);
    overflow: hidden;
    font-family: "Lato", sans-serif;
    color: var(--text-white);
  }
  .card__band {
    position: absolute; left: 0; right: 0; bottom: 0; height: 10px;
    background: var(--accent-red);
  }

  /* Front */
  .brand {
    position: absolute; left: 0; right: 0; top: 112px;
    display: flex; flex-direction: column; align-items: center;
  }
  .brand__row { display: flex; align-items: center; gap: 14px; }
  .brand__dot {
    width: 46px; height: 46px; border-radius: 50%;
    background: var(--accent-red);
  }
  .brand__name {
    font-weight: 900; font-size: 38px; letter-spacing: 1.5px;
    text-transform: uppercase; color: var(--text-white); white-space: nowrap;
  }
  .brand__tagline {
    margin-top: 12px; display: flex; align-items: center; gap: 12px;
    color: var(--accent-red); font-size: 14px; letter-spacing: 2px; text-transform: uppercase;
  }
  .brand__rule { width: 140px; height: 1px; background: var(--accent-red); }

  /* Back */
  .person {
    position: absolute; right: 352px; top: 138px; text-align: right;
  }
  .person__name {
    font-family: "Oswald", sans-serif; font-weight: 500;
    font-size: 32px; line-height: 1; text-transform: uppercase;
    color: var(--accent-red); letter-spacing: -.3px; white-space: nowrap;
  }
  .person__title { margin-top: 5px; font-size: 16px; letter-spacing: .5px; white-space: nowrap; }
  .divider {
    position: absolute; left: 268px; top: 124px; width: 1px; height: 100px;
    background: var(--divider);
  }
  .contacts {
    position: absolute; left: 288px; top: 132px;
    list-style: none; display: flex; flex-direction: column; gap: 9px;
  }
  .contacts__item { display: flex; align-items: center; gap: 9px; font-size: 16px; letter-spacing: .3px; white-space: nowrap; }
  .contacts__icon { width: 17px; height: 17px; flex: none; }
  .service-line {
    position: absolute; left: 40px; bottom: 36px;
    font-size: 16px; letter-spacing: .4px; white-space: nowrap;
  }
</style>
</head>
<body>
<main class="canvas">
  <section class="card card--front" aria-label="Business card front">
    <div class="brand">
      <div class="brand__row">
        <span class="brand__dot"></span>
        <span class="brand__name">Pecan Ridge Paving</span>
      </div>
      <div class="brand__tagline">
        <span class="brand__rule"></span>
        <span>Chip Seal Done Right</span>
      </div>
    </div>
    <div class="card__band"></div>
  </section>

  <section class="card card--back" aria-label="Business card back">
    <div class="person">
      <p class="person__name">Dale R. Whitmore</p>
      <p class="person__title">Managing Director</p>
    </div>
    <div class="divider"></div>
    <ul class="contacts">
      <li class="contacts__item">
        <svg class="contacts__icon" viewBox="0 0 24 24" aria-hidden="true"><path fill="#b21f2d" d="M6.6 10.8a15.1 15.1 0 0 0 6.6 6.6l2.2-2.2c.3-.3.7-.4 1-.2 1.1.4 2.3.6 3.6.6.6 0 1 .4 1 1V20c0 .6-.4 1-1 1A17 17 0 0 1 3 4c0-.6.4-1 1-1h3.5c.6 0 1 .4 1 1 0 1.3.2 2.5.6 3.6.1.3 0 .7-.2 1z"/></svg>
        <span>830.555.0173</span>
      </li>
      <li class="contacts__item">
        <svg class="contacts__icon" viewBox="0 0 24 24" aria-hidden="true"><path fill="#b21f2d" d="M2 5h20v14H2zm2 2v.4l8 5.2 8-5.2V7zm0 2.8V17h16V9.8l-8 5.2z"/></svg>
        <span>Dalewhitmore7@mailbarn.net</span>
      </li>
      <li class="contacts__item">
        <svg class="contacts__icon" viewBox="0 0 24 24" aria-hidden="true"><g fill="none" stroke="#b21f2d" stroke-width="2"><circle cx="12" cy="12" r="9"/><path d="M3 12h18M12 3c3 3 3 15 0 18M12 3c-3 3-3 15 0 18"/></g></svg>
        <span>www.pecanridgepaving.net</span>
      </li>
    </ul>
    <p class="service-line">Pecan Ridge’s Top Paving Company</p>
    <div class="card__band"></div>
  </section>
</main>
</body>
</html>
```